I need a audit of my current site.. with suggestions and actions

My current site, www.brickwisely does not support the high tech industry we are in. I am seeking knowledge, direction and action, I will pay hourly or by job. I also need SEO help, driven with impact trusted deliverable, our clients have to trust us to do our job. We are like Vorlin to the construction industry, gathering their data for the lifecycle. Eliminating litigation, un wanted change orders and providing audit ready projects. Eveyone wins

Target Market(s)

Construction industry, Federal and Private

Industry/Entity Type

Construction industry, globally

Coding

Coded - Design and coding required

Number of Pages Required

5+ page

Font styles to use
Sans Serif

Colors
EE7325
F08F49
F5BC92
FAE3D3
FDF4ED

Requirements
Must have
• High tech look
Should not have
• Misspelled words

```html
<!DOCTYPE html>
<html lang="en">
<head>
<meta charset="utf-8">
<title>BrickWisely — The Smartest Way To Build</title>
<link href="https://fonts.googleapis.com/css2?family=Montserrat:wght@500;600;700;800&family=Lato:wght@400;700&display=swap" rel="stylesheet">
<style>
:root{
  --orange:#EE7325;
  --orange-deep:#E85A1B;
  --orange-mid:#F08F49;
  --orange-soft:#F5BC92;
  --orange-pale:#FAE3D3;
  --cream:#FDF4ED;
  --ink:#1c1c1c;
  --charcoal:#4a4a4a;
  --dark:#151515;
  --grey-band:#f1f1f3;
  --line:#d9d9d9;
  --white:#ffffff;
}
*{margin:0;padding:0;box-sizing:border-box}
html,body{width:1200px;height:4461px;overflow:hidden}
body{position:relative;background:var(--white);font-family:'Lato',sans-serif;color:var(--ink)}
.abs{position:absolute}
.heading{font-family:'Montserrat',sans-serif;font-weight:700;letter-spacing:2px;text-transform:uppercase}
.eyebrow{font-family:'Montserrat',sans-serif;font-weight:600;font-size:14px;letter-spacing:1px;color:var(--orange);text-transform:uppercase;text-align:center;width:1200px;left:0}
.eyebrow::after{content:"";display:block;width:28px;height:2px;background:var(--orange);margin:6px auto 0}
.section-title{left:0;width:1200px;text-align:center;font-size:38px;line-height:47px;color:var(--ink)}

/* hero */
.hero{left:0;top:0;width:1200px;height:800px;background:linear-gradient(100deg,#141414 0%,#2a2a2a 45%,#5a5450 70%,#8a8580 100%)}
.hero-cutout{left:0;top:700px;width:1200px;height:110px}
.brand{font-family:'Montserrat',sans-serif;font-weight:600;font-size:27px;color:var(--white);display:flex;align-items:center;gap:8px}
.brand-mark{width:12px;height:12px;background:var(--orange)}
.brand-tag{font-size:9px;color:#cfcfcf;letter-spacing:.3px}
.nav{top:55px;left:374px;display:flex;gap:44px;font-size:15px;color:var(--white)}
.nav-phone{top:46px;left:902px;display:flex;align-items:center;gap:14px;color:var(--white);font-size:18px}
.icon-circle{width:42px;height:42px;border-radius:50%;background:var(--orange);display:flex;align-items:center;justify-content:center}
.hero-title{left:111px;top:206px;font-size:62px;line-height:62px;color:var(--white);letter-spacing:3px}
.hero-title .accent{color:var(--orange)}
.hero-sub{left:111px;top:342px;width:360px;font-size:15px;line-height:26px;color:#e8e8e8}
.hero-list{left:111px;top:410px;list-style:none;font-size:19px;line-height:34px;color:var(--white)}
.hero-list li::before{content:"";display:inline-block;width:8px;height:8px;border-radius:50%;background:var(--orange);margin-right:7px;vertical-align:middle}
.btn{background:var(--orange-deep);color:var(--white);font-family:'Montserrat',sans-serif;font-weight:700;text-transform:uppercase;display:flex;align-items:center;justify-content:center;border-radius:30px}
.hero-btn{left:111px;top:523px;width:176px;height:52px;font-size:14px}

/* about */
.about-copy{left:190px;top:977px;width:820px;text-align:center;font-size:15px;line-height:26px;color:#333}
.feature{width:300px;text-align:center;font-family:'Montserrat',sans-serif;font-weight:600;font-size:22px;line-height:33px;letter-spacing:1px;color:var(--ink)}
.feature-ring{width:228px;height:228px;border-radius:50%;border:3px dotted #555;margin:0 auto 14px;display:flex;align-items:center;justify-content:center}
.feature-ring.is-active{border-color:var(--orange)}
.feature-disc{width:200px;height:200px;border-radius:50%;background:var(--charcoal);display:flex;align-items:center;justify-content:center}
.is-active .feature-disc{background:var(--orange-deep)}
.slider-arrow{width:30px;height:30px;border-radius:50%;display:flex;align-items:center;justify-content:center}

/* panels */
.panel-label{font-family:'Montserrat',sans-serif;font-weight:600;font-size:20px;letter-spacing:1.5px;color:var(--white);text-transform:uppercase;text-align:center}

/* milestones */
.milestones{left:0;top:2122px;width:1200px;height:402px;background:var(--grey-band)}
.stat{width:240px;text-align:center}
.stat-num{font-family:'Montserrat',sans-serif;font-weight:700;font-size:48px;color:var(--orange-deep);line-height:56px}
.stat-label{font-family:'Montserrat',sans-serif;font-weight:500;font-size:15px;color:var(--ink);margin-top:10px}
.stat-rule{width:2px;height:170px;background:var(--line)}
.stat-dot{width:10px;height:10px;border-radius:50%;background:var(--orange-deep)}

/* video */
.videos{left:0;top:2524px;width:1200px;height:493px;background:linear-gradient(180deg,#1e1e1e,#2b2b2b)}
.video-frame{left:156px;top:2724px;width:888px;height:527px;border:3px solid var(--orange-deep);background:#e4e4e4}
.play{left:559px;top:2953px;width:70px;height:70px;border-radius:50%;background:var(--orange-deep);display:flex;align-items:center;justify-content:center}

/* contact */
.find-title{left:159px;top:3470px;font-size:24px;color:var(--ink)}
.info{left:159px;display:flex;gap:12px}
.info-label{font-family:'Montserrat',sans-serif;font-weight:700;font-size:14px;letter-spacing:.5px}
.info-text{font-size:15px;line-height:26px;color:#333;margin-top:6px}
.field{left:551px;width:488px;height:56px;background:var(--white);border:1px solid #eee;box-shadow:0 2px 10px rgba(0,0,0,.06);font-size:14px;color:#777;padding:18px 28px}
.submit{left:554px;top:3760px;width:154px;height:49px;font-size:14px;border-radius:3px}

/* partners */
.partners{left:95px;top:3880px;width:1010px;height:104px;background:#f7f7f7}
.badge{background:#bdbdbd}

/* footer */
.footer{left:0;top:4015px;width:1200px;height:446px}
.foot-head{font-size:21px;color:var(--white);letter-spacing:1.5px}
.foot-links{list-style:none;font-size:15px;line-height:30.5px;color:#e5e5e5}
.foot-links li::before{content:"«";color:var(--orange);margin-right:8px}
.social{width:28px;height:28px;border-radius:50%;background:#3a3a3a}
.social.is-primary{background:var(--orange-deep)}
.news-input{left:809px;top:4171px;width:277px;height:40px;border:1px solid #555;border-radius:4px;font-size:14px;color:#999;padding:10px 16px}
.news-btn{left:809px;top:4224px;width:277px;height:40px;font-size:14px;border-radius:4px;text-transform:none}
.copyright{left:0;width:1200px;top:4407px;text-align:center;font-size:14px;color:#e5e5e5}
</style>
</head>
<body>

<!-- HERO -->
<div class="abs hero" role="img" aria-label="Construction worker in a hard hat blended with a city skyline"></div>
<svg class="abs hero-cutout" width="1200" height="110" viewBox="0 0 1200 110" aria-hidden="true">
  <polygon points="0,42 1200,100 1200,110 0,110" fill="#fff"/>
</svg>

<div class="abs" style="left:110px;top:44px">
  <div class="brand"><span>BrickWisely</span><span class="brand-mark"></span></div>
  <div class="brand-tag" style="margin-left:38px">The Ultimate Construction Technology</div>
</div>
<nav class="abs nav"><span>What We Offer</span><span>Portfolio</span><span>About</span><span>Podcast</span><span>Blogs</span></nav>
<div class="abs nav-phone">
  <span class="icon-circle"><svg width="18" height="18" viewBox="0 0 24 24"><path d="M6.6 10.8a15 15 0 0 0 6.6 6.6l2.2-2.2a1 1 0 0 1 1-.25 11.4 11.4 0 0 0 3.6.57 1 1 0 0 1 1 1V20a1 1 0 0 1-1 1A17 17 0 0 1 3 4a1 1 0 0 1 1-1h3.5a1 1 0 0 1 1 1c0 1.25.2 2.45.57 3.6a1 1 0 0 1-.25 1z" fill="#fff"/></svg></span>
  <span>(555) 014-2280</span>
</div>

<h1 class="abs heading hero-title">The <span class="accent">Smartest</span><br><span class="accent">Way</span> to Build</h1>
<p class="abs hero-sub">Construction Management Software With Human Integration</p>
<ul class="abs hero-list">
  <li>Organized And Secure</li>
  <li>Planholders Team Notifications And Updates</li>
  <li>Safeguarded Against Litigation</li>
</ul>
<div class="abs btn hero-btn">Get Started</div>
<svg class="abs" style="left:113px;top:610px" width="64" height="160" viewBox="0 0 64 160" aria-hidden="true">
  <rect x="12" y="12" width="40" height="40" transform="rotate(45 32 32)" fill="none" stroke="#fff" stroke-width="2"/>
  <polyline points="26,30 32,36 38,30" fill="none" stroke="#fff" stroke-width="2"/>
  <line x1="32" y1="61" x2="32" y2="160" stroke="#fff" stroke-width="1.5"/>
</svg>

<!-- ABOUT -->
<div class="abs eyebrow" style="top:877px">About Us</div>
<h2 class="abs heading section-title" style="top:914px">Brick Wisely</h2>
<p class="abs about-copy">Our clients are seeing an 18 to 1 return on their investment with BrickWisely. Our software is paired with a Project Information Manager who improves project transparency, accountability, and ensures informed decision making. Deliver projects on time and under budget.</p>

<svg class="abs" style="left:0;top:1120px" width="1200" height="925" viewBox="0 0 1200 925" aria-hidden="true">
  <polygon points="1200,6 1200,520 918,520" fill="var(--orange-deep)"/>
</svg>

<div class="abs slider-arrow" style="left:96px;top:1196px;background:var(--orange-deep)"><svg width="12" height="12" viewBox="0 0 12 12"><polyline points="8,2 4,6 8,10" fill="none" stroke="#fff" stroke-width="2"/></svg></div>
<div class="abs slider-arrow" style="left:1073px;top:1196px;border:1px solid #ddd"><svg width="12" height="12" viewBox="0 0 12 12"><polyline points="4,2 8,6 4,10" fill="none" stroke="#bbb" stroke-width="2"/></svg></div>

<div class="abs feature" style="left:132px;top:1093px">
  <div class="feature-ring"><div class="feature-disc">
    <svg width="90" height="90" viewBox="0 0 90 90" fill="none" stroke="#fff" stroke-width="3"><rect x="18" y="14" width="50" height="66" rx="4"/><rect x="32" y="8" width="22" height="12" rx="3"/><path d="M28 36h6M28 50h6M28 64h6M40 36h18M40 50h18M40 64h14"/><circle cx="68" cy="28" r="12"/><polyline points="62,28 67,33 75,23"/></svg>
  </div></div>
  Dedicated Project Information Manager
</div>
<div class="abs feature is-active" style="left:451px;top:1093px">
  <div class="feature-ring is-active"><div class="feature-disc">
    <svg width="90" height="90" viewBox="0 0 90 90" fill="none" stroke="#fff" stroke-width="3"><rect x="30" y="12" width="46" height="60" rx="2"/><path d="M24 20v58h44"/><path d="M16 28l8 52 40 0"/><path d="M40 28h26M40 38h26M40 48h26M40 58h18"/></svg>
  </div></div>
  Audited And Vetted Documentation
</div>
<div class="abs feature" style="left:766px;top:1093px">
  <div class="feature-ring"><div class="feature-disc">
    <svg width="90" height="90" viewBox="0 0 90 90" fill="none" stroke="#fff" stroke-width="3"><circle cx="42" cy="48" r="30"/><circle cx="42" cy="48" r="20"/><circle cx="42" cy="48" r="9"/><path d="M42 48L72 18M64 18h8v-8M72 18v8h8"/></svg>
  </div></div>
  Risk Mitigation
</div>

<div class="abs eyebrow" style="top:1466px">Why We Are The</div>
<h2 class="abs heading section-title" style="top:1508px">Best Construction<br>Management Software</h2>

<!-- PANELS -->
<svg class="abs" style="left:0;top:1640px" width="1200" height="482" viewBox="0 0 1200 482" aria-hidden="true">
  <defs>
    <linearGradient id="p1" x1="0" y1="0" x2="0" y2="1"><stop offset="0" stop-color="#6b5a4e"/><stop offset="1" stop-color="#2a2220"/></linearGradient>
    <linearGradient id="p2" x1="0" y1="0" x2="0" y2="1"><stop offset="0" stop-color="#d9d3cd"/><stop offset=".45" stop-color="#F08F49"/><stop offset="1" stop-color="#E85A1B"/></linearGradient>
    <linearGradient id="p3" x1="0" y1="0" x2="0" y2="1"><stop offset="0" stop-color="#2c3e4a"/><stop offset="1" stop-color="#0e161c"/></linearGradient>
    <linearGradient id="p4" x1="0" y1="0" x2="0" y2="1"><stop offset="0" stop-color="#8a7d6a"/><stop offset="1" stop-color="#3b3730"/></linearGradient>
  </defs>
  <polygon points="0,0 250,0 284,404 0,404" fill="url(#p1)"/>
  <polygon points="260,0 563,0 598,404 294,404" fill="url(#p2)"/>
  <polygon points="572,0 875,0 909,404 610,404" fill="url(#p3)"/>
  <polygon points="883,0 1200,0 1200,404 921,404" fill="url(#p4)"/>
  <polygon points="704,404 866,404 818,482 658,482" fill="var(--orange-deep)"/>
</svg>
<div class="abs" role="img" aria-label="Portrait of a project manager in an office" style="left:0;top:1640px;width:250px;height:300px"></div>
<div class="abs" role="img" aria-label="Interlocking gears" style="left:300px;top:1640px;width:260px;height:150px"></div>
<div class="abs" role="img" aria-label="Server racks in a data centre" style="left:600px;top:1640px;width:270px;height:300px"></div>
<div class="abs" role="img" aria-label="Engineers in hard hats on a scaffolded site" style="left:900px;top:1640px;width:300px;height:300px"></div>

<div class="abs panel-label" style="left:14px;top:1978px;text-align:left">Project Managers</div>
<div class="abs panel-label" style="left:274px;top:1795px;width:300px;line-height:27px">Integration Across<br>The Board</div>
<p class="abs" style="left:294px;top:1862px;width:290px;text-align:center;font-size:13.5px;line-height:26px;color:#fff">The BrickWisely construction project management software handles every phase of your projects.</p>
<div class="abs" style="left:355px;top:1959px;width:153px;height:47px;background:#fff;border-radius:6px;display:flex;align-items:center;justify-content:center;font-family:'Montserrat',sans-serif;font-weight:700;font-size:14px;color:var(--orange-deep)">Learn More</div>
<div class="abs panel-label" style="left:610px;top:1981px;width:295px">Remove Data Silos</div>
<div class="abs panel-label" style="left:925px;top:1964px;width:285px;line-height:27px">Digital Twin Of Your<br>Asset Day One!</div>

<!-- MILESTONES -->
<div class="abs milestones"></div>
<div class="abs eyebrow" style="top:2176px">Countdown</div>
<h2 class="abs heading section-title" style="top:2210px">Milestones</h2>
<div class="abs stat" style="left:173px;top:2308px"><div class="stat-num">16</div><div class="stat-label">YEARS IN BUSINESS</div></div>
<div class="abs stat" style="left:446px;top:2308px"><div class="stat-num">+ 2 K</div><div class="stat-label">PROJECTS COMPLETED</div></div>
<div class="abs stat" style="left:723px;top:2308px"><div class="stat-num">$ 23 B</div><div class="stat-label">CONSTRUCTION VALUE</div></div>
<div class="abs stat-rule" style="left:422px;top:2290px"></div>
<div class="abs stat-rule" style="left:713px;top:2290px"></div>
<div class="abs stat-rule" style="left:962px;top:2290px"></div>
<div class="abs stat-dot" style="left:418px;top:2371px"></div>
<div class="abs stat-dot" style="left:709px;top:2371px"></div>
<div class="abs stat-dot" style="left:958px;top:2371px"></div>

<!-- VIDEO -->
<div class="abs videos"></div>
<div class="abs eyebrow" style="top:2562px">Our Videos</div>
<h2 class="abs heading section-title" style="top:2594px;color:#fff;width:1162px">Bridge The Gap In Project<br>Management Software</h2>
<div class="abs video-frame" role="img" aria-label="Hand-drawn whiteboard animation about bridging a gap with technology"></div>
<div class="abs play"><svg width="24" height="24" viewBox="0 0 24 24"><polygon points="7,4 20,12 7,20" fill="#fff"/></svg></div>

<!-- CONTACT -->
<div class="abs eyebrow" style="top:3321px">Get A Quote</div>
<h2 class="abs heading section-title" style="top:3351px">Contact Us</h2>
<h3 class="abs heading find-title">Where To Find Us</h3>

<div class="abs info" style="top:3526px">
  <svg width="18" height="18" viewBox="0 0 24 24"><path d="M12 2a7 7 0 0 0-7 7c0 5 7 13 7 13s7-8 7-13a7 7 0 0 0-7-7zm0 9.5A2.5 2.5 0 1 1 12 6.5a2.5 2.5 0 0 1 0 5z" fill="var(--orange-deep)"/></svg>
  <div><div class="info-label">ADDRESS</div><div class="info-text">218 Harlow Street Westbrook,<br>KS 66000</div></div>
</div>
<div class="abs info" style="top:3623px">
  <svg width="18" height="18" viewBox="0 0 24 24"><path d="M6.6 10.8a15 15 0 0 0 6.6 6.6l2.2-2.2a1 1 0 0 1 1-.25 11.4 11.4 0 0 0 3.6.57 1 1 0 0 1 1 1V20a1 1 0 0 1-1 1A17 17 0 0 1 3 4a1 1 0 0 1 1-1h3.5a1 1 0 0 1 1 1c0 1.25.2 2.45.57 3.6a1 1 0 0 1-.25 1z" fill="var(--orange-deep)"/></svg>
  <div><div class="info-label">PHONE</div><div class="info-text" style="font-weight:700;color:var(--ink)">(555) 014-2280</div></div>
</div>
<div class="abs info" style="top:3701px">
  <svg width="18" height="18" viewBox="0 0 24 24"><rect x="2" y="5" width="20" height="14" rx="2" fill="var(--orange-deep)"/><polyline points="3,7 12,13 21,7" fill="none" stroke="#fff" stroke-width="1.6"/></svg>
  <div><div class="info-label">EMAIL</div><div class="info-text" style="color:var(--orange-deep)">hello@brickwisely.com</div></div>
</div>

<div class="abs field" style="top:3450px">Name</div>
<div class="abs field" style="top:3525px">Phone</div>
<div class="abs field" style="top:3599px">Email</div>
<div class="abs field" style="top:3672px">Messages</div>
<div class="abs btn submit">Submit</div>

<!-- PARTNERS -->
<svg class="abs" style="left:45px;top:3920px" width="30" height="24" viewBox="0 0 30 24"><path d="M28 12H4M12 3l-9 9 9 9" fill="none" stroke="#666" stroke-width="2.5"/></svg>
<svg class="abs" style="left:1128px;top:3920px" width="30" height="24" viewBox="0 0 30 24"><path d="M2 12h24M18 3l9 9-9 9" fill="none" stroke="#666" stroke-width="2.5"/></svg>
<div class="abs partners"></div>
<div class="abs badge" style="left:136px;top:3896px;width:160px;height:72px;border-radius:6px"></div>
<div class="abs badge" style="left:337px;top:3904px;width:150px;height:52px;border-radius:4px"></div>
<div class="abs badge" style="left:518px;top:3912px;width:160px;height:40px;border-radius:20px"></div>
<div class="abs badge" style="left:708px;top:3914px;width:170px;height:36px;border-radius:4px"></div>
<div class="abs badge" style="left:905px;top:3912px;width:160px;height:40px;border-radius:4px"></div>

<!-- FOOTER -->
<svg class="abs footer" width="1200" height="446" viewBox="0 0 1200 446" aria-hidden="true">
  <polygon points="0,64 1200,0 1200,446 0,446" fill="var(--dark)"/>
</svg>
<div class="abs" style="left:109px;top:4133px">
  <div class="brand" style="font-size:30px"><span>BrickWisely</span><span class="brand-mark"></span></div>
  <div class="brand-tag" style="margin-left:46px">The Ultimate Construction Technology</div>
</div>
<div class="abs social is-primary" style="left:155px;top:4217px"></div>
<div class="abs social" style="left:192px;top:4217px"></div>
<div class="abs social" style="left:228px;top:4217px"></div>
<div class="abs social" style="left:265px;top:4217px"></div>

<h4 class="abs heading foot-head" style="left:404px;top:4121px">Quick Link</h4>
<ul class="abs foot-links" style="left:404px;top:4160px"><li>What We Offer</li><li>Portfolio</li><li>About</li><li>Podcast</li><li>Blogs</li></ul>
<h4 class="abs heading foot-head" style="left:594px;top:4121px">Help Link</h4>
<ul class="abs foot-links" style="left:594px;top:4160px"><li>Terms &amp; Conditions</li><li>Privacy Policy</li><li>About Us</li><li>Support</li></ul>
<h4 class="abs heading foot-head" style="left:809px;top:4121px">Get Our Newsletter</h4>
<div class="abs news-input">Enter Your Email</div>
<div class="abs btn news-btn">Subscribe Now</div>
<p class="abs copyright">©Copyrights 2022&nbsp; Brick Wisely |&nbsp;&nbsp; All Rights Reserved</p>

</body>
</html>
```